Brightmere email header for parts

We sell parts to the construction equipment industry. We want a header for our emails that reflect what we do. I will include what we have now but want something for parts only. Added a lot of pictures just so you can look through what we do.

```html
<!DOCTYPE html>
<html lang="en">
<head>
<meta charset="utf-8">
<title>Brightmere Email Headers – Parts</title>
<link rel="stylesheet" href="https://fonts.googleapis.com/css2?family=Teko:wght@300;400;600;700&display=swap">
<style>
  :root {
    --page-bg: #efefef;
    --red-deep: #8e0f0c;
    --red-mid: #c4231c;
    --red-bright: #e0332a;
    --black-band: #0c0c0c;
    --white: #ffffff;
    --phone-red: #e4231b;
    --parts-yellow: #e9cf2e;
    --parts-shade: #b99a18;
    --tank-yellow: #f2c63a;
  }
  html, body {
    margin: 0;
    padding: 0;
    width: 1200px;
    height: 815px;
    overflow: hidden;
    background: var(--page-bg);
  }
  .canvas {
    position: relative;
    width: 1200px;
    height: 815px;
  }
  .header-banner {
    position: absolute;
    left: 75px;
    width: 1050px;
    height: 322px;
    overflow: hidden;
    font-family: 'Teko', sans-serif;
  }
  .header-banner--parts { top: 69px; }
  .header-banner--component { top: 415px; }

  .warehouse-backdrop {
    position: absolute;
    inset: 0;
    background:
      linear-gradient(90deg, rgba(120,10,8,0.55) 0%, rgba(0,0,0,0) 45%, rgba(90,8,6,0.45) 100%),
      linear-gradient(180deg, var(--red-mid) 0%, var(--red-bright) 45%, var(--red-deep) 100%);
  }
  .product-photo {
    position: absolute;
    border-radius: 6px;
  }
  .header-banner--parts .product-photo {
    left: 510px;
    top: 22px;
    width: 535px;
    height: 270px;
    background: radial-gradient(ellipse at 55% 45%, var(--parts-yellow) 0%, var(--parts-shade) 60%, rgba(60,20,10,0.6) 100%);
  }
  .header-banner--component .product-photo {
    left: 540px;
    top: 95px;
    width: 440px;
    height: 150px;
    border-radius: 22px 22px 10px 10px;
    background: linear-gradient(180deg, var(--tank-yellow) 0%, #e0ad22 100%);
  }

  .brand-name {
    position: absolute;
    left: 0;
    width: 512px;
    top: 60px;
    display: flex;
    justify-content: center;
    align-items: center;
    gap: 8px;
    color: var(--white);
    font-weight: 600;
    font-size: 30px;
    line-height: 1;
    letter-spacing: 0.5px;
  }
  .brand-mark {
    width: 14px;
    height: 14px;
    background: var(--white);
  }
  .headline {
    position: absolute;
    left: 59px;
    color: var(--white);
    margin: 0;
    line-height: 1;
    white-space: nowrap;
    text-transform: uppercase;
  }
  .headline--services {
    top: 121px;
    font-weight: 400;
    font-size: 50px;
    letter-spacing: 0;
  }
  .headline--parts {
    top: 172px;
    font-weight: 700;
    font-size: 52px;
    letter-spacing: 0.6px;
    text-shadow: 0 2px 4px rgba(0,0,0,0.45);
  }
  .contact-band {
    position: absolute;
    left: 0;
    top: 238px;
    width: 520px;
    height: 84px;
  }
  .band-shape { position: absolute; left: 0; top: 0; }
  .phone-line {
    position: absolute;
    left: 63px;
    top: 0;
    height: 84px;
    display: flex;
    align-items: center;
    gap: 24px;
    color: var(--white);
    font-weight: 600;
    font-size: 58px;
    letter-spacing: 0.5px;
    line-height: 1;
  }
  .phone-icon { flex: none; display: block; }
  .phone-number { padding-top: 10px; }
</style>
</head>
<body>
<div class="canvas">

  <section class="header-banner header-banner--parts">
    <div class="warehouse-backdrop" role="img" aria-label="Red-tinted photo of a parts warehouse with shelving and workshop machinery"></div>
    <div class="product-photo" role="img" aria-label="Yellow construction equipment replacement parts: steering knuckle, final drive, sprocket and black bushings"></div>
    <div class="brand-name"><span class="brand-mark"></span>BRIGHTMERE</div>
    <p class="headline headline--services">Construction Equipment</p>
    <p class="headline headline--parts">Replacement Parts</p>
    <div class="contact-band">
      <svg class="band-shape" width="520" height="84" viewBox="0 0 520 84"><polygon points="0,0 482,0 520,84 0,84" fill="var(--black-band)"/></svg>
      <div class="phone-line">
        <svg class="phone-icon" width="32" height="34" viewBox="0 0 24 24" aria-hidden="true"><path fill="var(--phone-red)" d="M6.6 10.8a15.1 15.1 0 0 0 6.6 6.6l2.2-2.2a1 1 0 0 1 1-.25 11.4 11.4 0 0 0 3.6.57 1 1 0 0 1 1 1V20a1 1 0 0 1-1 1A17 17 0 0 1 3 4a1 1 0 0 1 1-1h3.5a1 1 0 0 1 1 1c0 1.25.2 2.45.57 3.57a1 1 0 0 1-.25 1z"/></svg>
        <span class="phone-number">555 014 2290</span>
      </div>
    </div>
  </section>

  <section class="header-banner header-banner--component">
    <div class="warehouse-backdrop" role="img" aria-label="Red-tinted photo of a parts warehouse with shelving and workshop machinery"></div>
    <div class="product-photo" role="img" aria-label="Large yellow heavy equipment body component with red and black stripes"></div>
    <div class="brand-name"><span class="brand-mark"></span>BRIGHTMERE</div>
    <p class="headline headline--services">Construction Equipment</p>
    <p class="headline headline--parts">Replacement Parts</p>
    <div class="contact-band">
      <svg class="band-shape" width="520" height="84" viewBox="0 0 520 84"><polygon points="0,0 482,0 520,84 0,84" fill="var(--black-band)"/></svg>
      <div class="phone-line">
        <svg class="phone-icon" width="32" height="34" viewBox="0 0 24 24" aria-hidden="true"><path fill="var(--phone-red)" d="M6.6 10.8a15.1 15.1 0 0 0 6.6 6.6l2.2-2.2a1 1 0 0 1 1-.25 11.4 11.4 0 0 0 3.6.57 1 1 0 0 1 1 1V20a1 1 0 0 1-1 1A17 17 0 0 1 3 4a1 1 0 0 1 1-1h3.5a1 1 0 0 1 1 1c0 1.25.2 2.45.57 3.57a1 1 0 0 1-.25 1z"/></svg>
        <span class="phone-number">555 014 2290</span>
      </div>
    </div>
  </section>

</div>
</body>
</html>
```